Design Home Screen

We’re looking for talented UI/UX designers to create an eye-popping, modern, and fun Home Screen for the Plenk app — the future of real-time earned wage access and financial empowerment.
Your mission: make the Plenk experience come alive the moment users open the app.

Design Goals

The screen should instantly communicate energy, financial control, and trust.

The “Time on the Clock” and the “Plenk Balance” must be the stars of the screen — presented in a way that feels alive, interactive, and rewarding.

Think of how to visually celebrate a user’s progress at work and their earnings — something that makes checking the app feel fun and satisfying, not transactional.

Creative Direction

Style: Sleek, fintech-modern, with motion or visual elements that feel alive (micro-animations, glowing accents, gradient depth, or movement cues).

Tone: Confident, vibrant, and optimistic — this is a financial app that feels human and inspiring.

Color palette: Black, Gold, and Green, and any other color.

Typography: Clean, readable, and balanced between playful and professional.

Must-Have Elements

Time on the Clock – creatively displayed (e.g., countdown or progress animation as the user works).

Plenk Balance – bold, fun, and maybe even interactive (reflecting growth as the user earns).

A clean navigation structure for core tabs: Home, Access Pay, Boost, History, Profile.

Engaging micro-animations, icons, or progress indicators that make the user feel “in motion.”

Room for brand personality — the “Plenk” name and logo if desired.

```html
<!DOCTYPE html>
<html lang="en">
<head>
<meta charset="utf-8">
<title>Plenk Home</title>
<link rel="stylesheet" href="https://fonts.googleapis.com/css2?family=Inter:wght@400;500;600;700&display=swap">
<style>
  :root{
    --page:#334158;
    --screen:#131316;
    --nav:#1b1c22;
    --white:#ffffff;
    --muted:#9a9ca8;
    --gold:#fbbf14;
    --green:#2ec4a0;
    --mint:#3fd6b0;
    --blue:#2b4bff;
    --sky:#2aa4f0;
    --chip:#2c2f3a;
    --accent:#5b7cff;
  }
  *{margin:0;padding:0;box-sizing:border-box}
  html,body{width:818px;height:1200px;overflow:hidden;background:var(--page);font-family:"Inter",sans-serif;color:var(--white)}
  .screen{position:absolute;left:142px;top:22px;width:534px;height:1155px;border-radius:44px;overflow:hidden;
    background:
      radial-gradient(ellipse 340px 300px at 380px 640px, rgba(88,40,150,.55), transparent 70%),
      radial-gradient(ellipse 320px 280px at 120px 640px, rgba(18,60,140,.6), transparent 70%),
      var(--screen);}
  .abs{position:absolute}
  .status-time{left:37px;top:30px;font-size:24px;font-weight:600}
  .status-icons{right:26px;top:33px;display:flex;gap:8px;align-items:center}
  .avatar{left:24px;top:110px;width:61px;height:61px;border-radius:14px;background:#1f2a44;border:1px solid #33405e;display:flex;align-items:center;justify-content:center;font-size:24px;font-weight:600}
  .welcome{left:103px;top:114px;font-size:19px;color:var(--muted);line-height:28px}
  .welcome b{display:block;color:var(--white);font-weight:600}
  .boost{left:333px;top:120px;width:123px;height:41px;border:2px solid var(--gold);border-radius:21px;color:var(--gold);font-size:19px;font-weight:600;display:flex;align-items:center;justify-content:center;gap:12px}
  .bell{left:469px;top:120px;width:42px;height:42px;border-radius:50%;background:#2a2b31;display:flex;align-items:center;justify-content:center}
  .bell::after{content:"";position:absolute;right:6px;top:5px;width:10px;height:10px;border-radius:50%;background:#ff4d5e}
  .balance-card{left:23px;top:206px;width:487px;height:324px;border-radius:28px;overflow:hidden;background:#2d2c55}
  .balance-top{height:230px;background:linear-gradient(115deg,#2347ff 0%,#2a3ed0 35%,#1b2a70 60%,#2aa4f0 100%);text-align:center;position:relative}
  .balance-label{padding-top:24px;font-size:17px;display:flex;justify-content:center;align-items:center;gap:8px}
  .balance-amount{font-size:51px;font-weight:700;margin-top:16px;letter-spacing:-1px}
  .active-pill{position:absolute;left:79px;top:128px;width:330px;height:36px;border-radius:18px;background:#eef1ff;border:2px solid #9fb2ff;display:flex;align-items:center;padding-left:10px;gap:6px;color:var(--accent);font-size:16px;font-weight:500;white-space:nowrap}
  .rate{margin-left:auto;margin-right:3px;background:var(--green);color:var(--white);border-radius:15px;padding:4px 10px;font-weight:600}
  .period{position:absolute;left:0;right:0;top:182px;font-size:17px;display:flex;justify-content:center;gap:8px;align-items:center;white-space:nowrap}
  .hours-icon{left:18px;top:248px;width:58px;height:58px;border-radius:12px;background:#1c2450;border:1px solid #4b5ba8;display:flex;align-items:center;justify-content:center}
  .hours-text{left:88px;top:250px}
  .hours-label{font-size:17px;color:#c9cad6}
  .hours-value{font-size:24px;font-weight:700;margin-top:6px}
  .clock-btn{left:320px;top:259px;width:150px;height:36px;border:2px solid var(--mint);border-radius:18px;color:var(--mint);font-size:17px;font-weight:500;display:flex;align-items:center;justify-content:center;gap:10px;white-space:nowrap}
  .dot{width:10px;height:10px;border-radius:50%;background:var(--mint)}
  .action{top:565px;width:90px;text-align:center}
  .action .ring{width:85px;height:85px;border-radius:50%;margin:0 auto;background:rgba(70,80,130,.45);display:flex;align-items:center;justify-content:center}
  .action span{display:block;margin-top:16px;font-size:18px;font-weight:500}
  .tx-title{left:24px;top:722px;font-size:22px;font-weight:600}
  .see-all{right:24px;top:724px;display:flex;gap:20px;align-items:center;color:var(--accent);font-size:18px}
  .tx{left:24px;width:487px;height:56px}
  .tx-icon{position:absolute;left:0;top:0;width:56px;height:56px;border-radius:14px;background:#22242c;border:1px solid #3a3d48;display:flex;align-items:center;justify-content:center}
  .tx-name{position:absolute;left:77px;top:2px;font-size:20px;font-weight:600}
  .tx-date{position:absolute;left:77px;top:33px;font-size:17px;color:var(--muted)}
  .tx-amount{position:absolute;right:0;top:2px;font-size:21px;font-weight:600;display:flex;align-items:center;gap:14px}
  .tx-amount.sent{color:var(--mint)}
  .tx-amount.pending{color:#e8f6f2}
  .tx-amount i{width:8px;height:8px;border-radius:50%;background:var(--mint)}
  .tx-status{position:absolute;right:0;top:33px;font-size:17px;color:#d7d8de}
  .nav{left:0;top:1013px;width:534px;height:142px;background:var(--nav)}
  .nav-item{position:absolute;top:16px;width:90px;text-align:center;font-size:17px}
  .nav-item svg{display:block;margin:0 auto 10px}
  .nav-item.active{color:var(--accent);font-weight:600}
  .nav-center{position:absolute;left:233px;top:14px;width:68px;height:68px;border-radius:50%;background:var(--gold);display:flex;align-items:center;justify-content:center}
  .home-bar{position:absolute;left:162px;top:126px;width:210px;height:6px;border-radius:3px;background:#d4d5da}
</style>
</head>
<body>
<main class="screen">
  <div class="abs status-time">9:41</div>
  <div class="abs status-icons">
    <svg width="28" height="18" viewBox="0 0 28 18"><g fill="#fff"><rect x="0" y="12" width="5" height="6" rx="1"/><rect x="7" y="8" width="5" height="10" rx="1"/><rect x="14" y="4" width="5" height="14" rx="1"/><rect x="21" y="0" width="5" height="18" rx="1"/></g></svg>
    <svg width="24" height="18" viewBox="0 0 24 18" fill="none" stroke="#fff" stroke-width="2.6" stroke-linecap="round"><path d="M2 6a14 14 0 0 1 20 0M6 10a8 8 0 0 1 12 0"/><circle cx="12" cy="15" r="1.5" fill="#fff"/></svg>
    <svg width="38" height="20" viewBox="0 0 38 20"><rect x="1" y="1" width="32" height="18" rx="5" fill="none" stroke="#888" stroke-width="1.5"/><rect x="3" y="3" width="22" height="14" rx="3" fill="#2ec4a0"/><rect x="35" y="7" width="2" height="6" rx="1" fill="#888"/><path d="M19 3l-6 8h5l-2 6 7-9h-5z" fill="#fff"/></svg>
  </div>

  <div class="abs avatar">JD</div>
  <div class="abs welcome">Welcome,<b>John Doe</b></div>
  <div class="abs boost">Boost
    <svg width="20" height="20" viewBox="0 0 24 24" fill="none" stroke="currentColor" stroke-width="2" stroke-linejoin="round"><path d="M14 4c3-2 6-2 6-2s0 3-2 6l-6 6-4-4z"/><path d="M8 10H4l3-3h4M14 16v4l3-3v-4M6 16c-2 1-2 4-2 4s3 0 4-2"/></svg>
  </div>
  <div class="abs bell">
    <svg width="24" height="24" viewBox="0 0 24 24" fill="none" stroke="#fff" stroke-width="2" stroke-linecap="round"><path d="M6 16V11a6 6 0 0 1 12 0v5l2 2H4z"/><path d="M10 21h4"/></svg>
  </div>

  <section class="abs balance-card">
    <div class="balance-top">
      <div class="balance-label">Plenk Wage Balance
        <svg width="20" height="16" viewBox="0 0 24 18" fill="none" stroke="#fff" stroke-width="2"><path d="M1 9s4-7 11-7 11 7 11 7-4 7-11 7S1 9 1 9z"/><circle cx="12" cy="9" r="3"/></svg>
      </div>
      <div class="balance-amount">$607.85</div>
      <div class="active-pill">
        <svg width="20" height="20" viewBox="0 0 24 24" fill="none" stroke="currentColor" stroke-width="2" stroke-linejoin="round"><path d="M14 4c3-2 6-2 6-2s0 3-2 6l-6 6-4-4z"/><path d="M8 10H4l3-3h4M14 16v4l3-3v-4M6 16c-2 1-2 4-2 4s3 0 4-2"/></svg>
        <span>Your Plenk is active!</span><span class="rate">+$21.90/hr</span>
      </div>
      <div class="period">
        <svg width="16" height="16" viewBox="0 0 24 24" fill="none" stroke="#fff" stroke-width="2"><rect x="3" y="5" width="18" height="16" rx="2"/><path d="M3 10h18M8 3v4M16 3v4"/></svg>
        Current Pay Period · Mar 1 – 15, 2025
      </div>
    </div>
    <div class="abs hours-icon">
      <svg width="30" height="26" viewBox="0 0 30 26"><g fill="#fff"><rect x="0" y="7" width="6" height="2.5" rx="1"/><rect x="0" y="12" width="4" height="2.5" rx="1"/><rect x="0" y="17" width="6" height="2.5" rx="1"/><circle cx="18" cy="13" r="11"/></g><path d="M18 7v6l4 3" stroke="#1c2450" stroke-width="2.5" fill="none" stroke-linecap="round"/></svg>
    </div>
    <div class="abs hours-text">
      <div class="hours-label">Work Hours</div>
      <div class="hours-value">27h 45m 20s</div>
    </div>
    <div class="abs clock-btn"><span class="dot"></span>On the Clock</div>
  </section>

  <div class="abs action" style="left:25px">
    <div class="ring"><svg width="28" height="30" viewBox="0 0 24 26" fill="none" stroke="#fff" stroke-width="2.2" stroke-linejoin="round"><rect x="2" y="4" width="20" height="20" rx="1"/><path d="M9 4V2h6v2M12 9v9M8 14l4 4 4-4"/></svg></div>
    <span>Request</span>
  </div>
  <div class="abs action" style="left:156px">
    <div class="ring"><svg width="28" height="28" viewBox="0 0 24 24" fill="none" stroke="#fff" stroke-width="2.2" stroke-linejoin="round"><path d="M8 3h8l-2 4c4 2 6 6 6 9a5 5 0 0 1-5 5H9a5 5 0 0 1-5-5c0-3 2-7 6-9z"/><circle cx="12" cy="15" r="2.5"/></svg></div>
    <span>Loan</span>
  </div>
  <div class="abs action" style="left:287px">
    <div class="ring"><svg width="30" height="30" viewBox="0 0 24 24" fill="none" stroke="#fff" stroke-width="2" stroke-linejoin="round"><path d="M6 18V3h12v8"/><path d="M9 7h6M9 10h6M3 18h10v3H5a2 2 0 0 1-2-2zM14 20l7-7-2-2-7 7v2z"/></svg></div>
    <span>Update</span>
  </div>
  <div class="abs action" style="left:418px">
    <div class="ring"><svg width="32" height="32" viewBox="0 0 24 24" fill="none" stroke="#fff" stroke-width="2" stroke-linecap="round"><path d="M4 12a8 8 0 0 1 14-5M20 12a8 8 0 0 1-14 5M18 3v4h-4M6 21v-4h4"/><path d="M14.5 9.5c-.5-1-1.5-1.5-2.5-1.5-1.4 0-2.5.8-2.5 2s1.1 1.6 2.5 2 2.5.8 2.5 2-1.1 2-2.5 2c-1 0-2-.5-2.5-1.5M12 6.5V8M12 16v1.5"/></svg></div>
    <span>Earn</span>
  </div>

  <h2 class="abs tx-title">Transactions</h2>
  <div class="abs see-all">See All
    <svg width="24" height="22" viewBox="0 0 24 22" fill="none" stroke="currentColor" stroke-width="1.8"><path d="M1 4h22M1 11h22M1 18h22"/><circle cx="15" cy="4" r="2.5" fill="#131316"/><circle cx="8" cy="11" r="2.5" fill="#131316"/><circle cx="14" cy="18" r="2.5" fill="#131316"/></svg>
  </div>

  <div class="abs tx" style="top:774px">
    <div class="tx-icon"><svg width="30" height="30" viewBox="0 0 24 24" fill="none" stroke="#fff" stroke-width="2" stroke-linecap="round"><circle cx="12" cy="12" r="10"/><path d="M12 17V7M8 11l4-4 4 4"/></svg></div>
    <div class="tx-name">John Doe Inc.</div><div class="tx-date">March 12, 2025</div>
    <div class="tx-amount sent"><i></i>$350.50</div><div class="tx-status">Sent</div>
  </div>
  <div class="abs tx" style="top:874px">
    <div class="tx-icon"><svg width="22" height="24" viewBox="0 0 20 24" fill="#fff"><rect x="2" y="1" width="16" height="3"/><rect x="2" y="20" width="16" height="3"/><path d="M4 4h12c0 4-4 6-4 8s4 4 4 8H4c0-4 4-6 4-8S4 8 4 4z"/></svg></div>
    <div class="tx-name">Taskhive</div><div class="tx-date">March 8, 2025</div>
    <div class="tx-amount pending"><i></i>$1,300.00</div><div class="tx-status">Pending</div>
  </div>
  <div class="abs tx" style="top:973px">
    <div class="tx-icon"><svg width="30" height="30" viewBox="0 0 24 24" fill="none" stroke="#fff" stroke-width="2" stroke-linecap="round"><circle cx="12" cy="12" r="10"/><path d="M12 17V7M8 11l4-4 4 4"/></svg></div>
    <div class="tx-name">Blooming Sales</div><div class="tx-date">March 2, 2025</div>
    <div class="tx-amount sent"><i></i>$75.00</div><div class="tx-status">Sent</div>
  </div>

  <nav class="abs nav">
    <div class="nav-item active" style="left:25px">
      <svg width="32" height="30" viewBox="0 0 24 22"><path d="M12 1L1 10h3v11h6v-6h4v6h6V10h3z" fill="#5b7cff"/></svg>Home
    </div>
    <div class="nav-item" style="left:124px">
      <svg width="26" height="30" viewBox="0 0 22 24" fill="none" stroke="#fff" stroke-width="2"><rect x="1" y="2" width="20" height="20" rx="1"/><path d="M7 17v-4M11 17v-8M15 17v-6"/></svg>Activity
    </div>
    <div class="nav-center">
      <svg width="38" height="38" viewBox="0 0 24 24" fill="none" stroke="#fff" stroke-width="2" stroke-linecap="round"><path d="M4 12a8 8 0 0 1 14-5M20 12a8 8 0 0 1-14 5M18 3v4h-4M6 21v-4h4"/><path d="M14.5 9.5c-.5-1-1.5-1.5-2.5-1.5-1.4 0-2.5.8-2.5 2s1.1 1.6 2.5 2 2.5.8 2.5 2-1.1 2-2.5 2c-1 0-2-.5-2.5-1.5M12 6.5V8M12 16v1.5"/></svg>
    </div>
    <div class="nav-item" style="left:320px">
      <svg width="30" height="30" viewBox="0 0 24 24" fill="none" stroke="#fff" stroke-width="2" stroke-linecap="round"><circle cx="12" cy="12" r="10"/><path d="M9.5 9a2.5 2.5 0 1 1 3.5 2.3c-.7.4-1 .9-1 1.7"/><circle cx="12" cy="17" r=".8" fill="#fff"/></svg>Help
    </div>
    <div class="nav-item" style="left:419px">
      <svg width="28" height="30" viewBox="0 0 24 24" fill="none" stroke="#fff" stroke-width="2"><circle cx="12" cy="7" r="4"/><path d="M3 22v-2a5 5 0 0 1 5-5h8a5 5 0 0 1 5 5v2z"/></svg>User
    </div>
    <div class="home-bar"></div>
  </nav>
</main>
</body>
</html>
```